Virtual Reality immersive experiences

Print ad 8.5" X 11"
Advertising to have people come rent time in our virtual reality room.
Fun for all ages
Unique experience
Immersive experience into 3D world
Escape reality
Be at heart of action - bottom of the ocean, travel the world, fight the invaders, solve the mystery and so much more
System used is Brelvo Optra
Dedicated room
Family friendly
$24 half hour
$40 per hour
Updates

Industry/Entity Type

Advertising

Requirements
Must have
• Be fun looking
• Eye catching
• Great pictures of VR experiences
• Pricing is $24 / 30 minutes and $40 / 1 hour
• Our location: 587 Larch Avenue, Three Hills, Alberta
• Our contact: 403-618-2093
• I have attached TERMALDO Technology Solutions logo which should be somewhere on the ad.
Nice to have
• could use phrases like: travel the world, explore the ocean depths, fight the invaders, visit the carnival

```html
<!DOCTYPE html>
<html lang="en">
<head>
<meta charset="utf-8">
<title>Virtual Reality – TERMALDO Technology Solutions</title>
<link rel="stylesheet" href="https://fonts.googleapis.com/css2?family=Josefin+Sans:wght@300;400;600&family=Roboto:wght@400;700&family=Roboto+Condensed:wght@700&display=swap">
<style>
  :root {
    --page: #e4e4e6;
    --ink: #1d1a2c;
    --title: rgba(205, 198, 235, 0.85);
    --white: #ffffff;
    --price: #a5141d;
    --price-label: #3f6fa8;
    --brand: #1c1a46;
    --sky-top: #3e4a92;
    --sky-mid: #8d72ba;
    --mist: #cfe2f1;
  }
  * { margin: 0; padding: 0; box-sizing: border-box; }
  html, body { width: 1200px; height: 1200px; overflow: hidden; }
  body { background: var(--page); position: relative; font-family: "Josefin Sans", sans-serif; color: var(--ink); }

  .poster { position: absolute; left: 152px; top: 20px; width: 896px; height: 1160px; overflow: hidden; }
  .poster-backdrop {
    position: absolute; inset: 0;
    background:
      radial-gradient(ellipse 45% 30% at 85% 62%, rgba(213,138,99,0.75), transparent 70%),
      radial-gradient(ellipse 55% 35% at 70% 50%, rgba(217,143,180,0.7), transparent 70%),
      radial-gradient(ellipse 40% 30% at 25% 68%, rgba(240,245,255,0.55), transparent 70%),
      linear-gradient(180deg, var(--sky-top) 0%, #6a66b0 22%, var(--sky-mid) 45%, #a9a8d6 68%, var(--mist) 85%, #d8e8f5 100%);
  }

  .title { position: absolute; left: 46px; top: 30px; font-weight: 300; font-size: 96px; letter-spacing: 1px; line-height: 1; color: var(--title); white-space: nowrap; }
  .tagline { position: absolute; left: 148px; top: 146px; font-weight: 400; font-size: 48px; line-height: 1; color: var(--white); white-space: nowrap; }

  .scene { position: absolute; border-radius: 50%; border: 3px solid var(--white); width: 170px; height: 170px; }
  .scene--ocean { left: 83px; top: 266px; background: radial-gradient(circle at 50% 30%, #5fb6d8, #1b6e9c 60%, #0d4a78); }
  .scene--world { left: 356px; top: 307px; background: linear-gradient(180deg, #d6ecf7 0%, #bfa98a 55%, #6aa15a 80%, #3a8fb8 100%); }
  .scene--invaders { left: 505px; top: 461px; background: linear-gradient(160deg, #e9e7e2 0%, #a89d86 50%, #5c5a4f 100%); }
  .scene--mystery { left: 421px; top: 658px; background: radial-gradient(circle at 50% 40%, #d9dde6, #9c8fae 55%, #6a3f6e 100%); }

  .caption { position: absolute; line-height: 1.1; white-space: nowrap; color: var(--ink); }
  .caption--ocean { left: 248px; top: 224px; font-size: 35px; }
  .caption--world { left: 545px; top: 312px; font-size: 46px; line-height: 1.2; }
  .caption--invaders { left: 689px; top: 493px; font-size: 33px; }
  .caption--mystery { left: 627px; top: 662px; font-size: 37px; }
  .caption--mystery .big { font-size: 47px; }
  .more { position: absolute; left: 593px; top: 796px; font-size: 28px; color: var(--ink); }

  .features { position: absolute; left: 75px; top: 867px; list-style: none; font-size: 21px; line-height: 27px; }
  .features li { display: flex; align-items: center; gap: 10px; white-space: nowrap; }
  .features svg { width: 21px; height: 21px; }

  .headset { position: absolute; left: 368px; top: 905px; width: 225px; height: 120px; border-radius: 40px 60px 30px 50px; background: radial-gradient(ellipse at 40% 50%, #3d5258, #141c20 75%, transparent 76%); }

  .price { position: absolute; left: 636px; display: flex; align-items: center; gap: 14px; }
  .price--half { top: 842px; }
  .price--hour { top: 938px; }
  .price-amount { font-family: "Roboto Condensed", sans-serif; font-weight: 700; font-size: 80px; color: var(--price); line-height: 1; letter-spacing: -2px; }
  .price-label { font-family: "Roboto", sans-serif; font-size: 26px; line-height: 1.1; color: var(--price-label); }

  .brand { position: absolute; left: 57px; top: 1058px; color: var(--brand); font-weight: 600; }
  .brand-name { font-size: 58px; letter-spacing: 2px; line-height: 1; display: block; }
  .brand-sub { font-size: 19px; letter-spacing: 3.4px; display: block; margin-top: 4px; }

  .contact { position: absolute; left: 445px; top: 1055px; font-family: "Roboto", sans-serif; color: var(--ink); }
  .contact-address { font-size: 23px; }
  .contact-phone { font-size: 30px; font-weight: 700; margin-top: 4px; }
</style>
</head>
<body>
  <main class="poster">
    <div class="poster-backdrop" role="img" aria-label="Smiling woman wearing a VR headset against a starry purple sky"></div>

    <h1 class="title">VIRTUAL REALITY</h1>
    <p class="tagline">BE AT HEART OF ACTION -</p>

    <div class="scene scene--ocean" role="img" aria-label="Underwater view of the ocean floor"></div>
    <p class="caption caption--ocean">BOTTOM OF<br>THE OCEAN</p>

    <div class="scene scene--world" role="img" aria-label="World landmarks collage"></div>
    <p class="caption caption--world">TRAVEL<br>THE WORLD</p>

    <div class="scene scene--invaders" role="img" aria-label="Soldiers in combat gear"></div>
    <p class="caption caption--invaders">FIGHT THE<br>INVADERS</p>

    <div class="scene scene--mystery" role="img" aria-label="Lone figure in a misty forest"></div>
    <p class="caption caption--mystery">SOLVE THE<br><span class="big">MYSTERY</span></p>

    <p class="more">And so much more</p>

    <ul class="features">
      <li><svg viewBox="0 0 24 24"><path d="M3 13l6 6L21 4" fill="none" stroke="#1d1a2c" stroke-width="4"/></svg>System used is Brelvo Optra</li>
      <li><svg viewBox="0 0 24 24"><path d="M3 13l6 6L21 4" fill="none" stroke="#1d1a2c" stroke-width="4"/></svg>Dedicated room</li>
      <li><svg viewBox="0 0 24 24"><path d="M3 13l6 6L21 4" fill="none" stroke="#1d1a2c" stroke-width="4"/></svg>Family friendly</li>
    </ul>

    <div class="headset" role="img" aria-label="Brelvo Optra VR headset"></div>

    <div class="price price--half"><span class="price-amount">$24</span><span class="price-label">HALF<br>HOUR</span></div>
    <div class="price price--hour"><span class="price-amount">$40</span><span class="price-label">PER<br>HOUR</span></div>

    <div class="brand">
      <span class="brand-name">TERMALDO</span>
      <span class="brand-sub">TECHNOLOGY SOLUTIONS</span>
    </div>

    <div class="contact">
      <p class="contact-address">587 Larch Avenue, Three Hills, Alberta</p>
      <p class="contact-phone">Call Us Now 403-618-2093</p>
    </div>
  </main>
</body>
</html>
```